Business card design reauest

2 sided. White on both sides

Martin Oakhurst

Ho Chi Minh, Vietnam

Cell Phone / Whatsapp/ Wechat/Zalo
1-555-382-7194
Moakhurst@kvpartsline.vn
Www.kvpartsline.vn
Www.kvpartsline.com

Industry/Entity Type

Sofa and furniture and kitchen

Contact Information for Business Card

2 sided. White on both sides Martin Oakhurst Ho Chi Minh, Vietnam Cell Phone / Whatsapp/ Wechat/Zalo 1-555-382-7194 Moakhurst@kvpartsline.vn Www.kvpartsline.vn Www.kvpartsline.com

```html
<!DOCTYPE html>
<html lang="en">
<head>
<meta charset="utf-8">
<title>KV Parts Line – Business Card</title>
<link href="https://fonts.googleapis.com/css2?family=Cinzel:wght@600&family=Tinos&display=swap" rel="stylesheet">
<style>
  :root {
    --page: #141516;
    --card: #ffffff;
    --card-edge: #f3f4f3;
    --green: #1c9c3c;
    --ink: #2b2b2d;
    --rule: #6a6a6d;
  }
  * { box-sizing: border-box; margin: 0; padding: 0; }
  html, body { width: 1200px; height: 840px; overflow: hidden; }
  body {
    background: var(--page);
    display: flex;
    flex-direction: column;
    align-items: center;
    justify-content: center;
    gap: 36px;
    font-family: "Tinos", "Times New Roman", serif;
    color: var(--ink);
  }
  .card {
    position: relative;
    width: 620px;
    height: 354px;
    border-radius: 22px;
    background: linear-gradient(135deg, var(--card) 0%, var(--card-edge) 100%);
    border: 2px solid var(--green);
    overflow: hidden;
  }
  /* back side */
  .card--back {
    display: flex;
    align-items: center;
    justify-content: center;
  }
  .brand-name {
    font-family: "Cinzel", "Times New Roman", serif;
    font-weight: 600;
    color: var(--green);
    letter-spacing: 1px;
    white-space: nowrap;
  }
  .card--back .brand-name { font-size: 40px; }
  /* front side */
  .brand {
    position: absolute;
    top: 46px;
    right: 44px;
    display: flex;
    align-items: center;
    gap: 14px;
  }
  .brand-mark {
    width: 26px;
    height: 26px;
    background: var(--green);
  }
  .card--front .brand-name { font-size: 30px; }
  .address {
    position: absolute;
    top: 150px;
    right: 44px;
    text-align: right;
    font-size: 17px;
    line-height: 1.3;
    color: var(--ink);
  }
  .holder {
    position: absolute;
    left: 44px;
    bottom: 44px;
    width: 330px;
  }
  .holder-name {
    font-family: "Cinzel", "Times New Roman", serif;
    font-weight: 600;
    font-size: 22px;
    color: var(--green);
    letter-spacing: 0.5px;
    padding-bottom: 8px;
    border-bottom: 1px solid var(--rule);
    margin-bottom: 12px;
  }
  .contact-list { list-style: none; }
  .contact-item {
    display: flex;
    align-items: center;
    gap: 10px;
    font-size: 16px;
    line-height: 1.45;
    color: var(--ink);
  }
  .contact-icon { width: 14px; height: 14px; flex: none; }
</style>
</head>
<body>

<section class="card card--back" aria-label="Card back">
  <span class="brand-name">KV Parts Line</span>
</section>

<section class="card card--front" aria-label="Card front">
  <div class="brand">
    <span class="brand-mark"></span>
    <span class="brand-name">KV Parts Line</span>
  </div>

  <p class="address">Ho Chi Minh<br>Vietnam</p>

  <div class="holder">
    <h1 class="holder-name">Martin Oakhurst</h1>
    <ul class="contact-list">
      <li class="contact-item">
        <svg class="contact-icon" viewBox="0 0 16 16" aria-hidden="true"><path fill="#1c9c3c" d="M3.5 1.5l2.5 0 1 3.5-1.7 1.2a9 9 0 0 0 4.5 4.5L11 9l3.5 1v2.5c0 1-1 2-2 2C6.5 14.5 1.5 9.5 1.5 3.5c0-1 1-2 2-2z"/></svg>
        <span>1-555-382-7194</span>
      </li>
      <li class="contact-item">
        <svg class="contact-icon" viewBox="0 0 16 16" aria-hidden="true"><rect x="1" y="3" width="14" height="10" rx="1" fill="#1c9c3c"/><path d="M1.5 3.8L8 9l6.5-5.2" fill="none" stroke="#ffffff" stroke-width="1.3"/></svg>
        <span>Moakhurst@kvpartsline.vn</span>
      </li>
      <li class="contact-item">
        <svg class="contact-icon" viewBox="0 0 16 16" aria-hidden="true"><circle cx="8" cy="8" r="6.5" fill="none" stroke="#1c9c3c" stroke-width="1.5"/><ellipse cx="8" cy="8" rx="2.8" ry="6.5" fill="none" stroke="#1c9c3c" stroke-width="1.2"/><path d="M1.5 8h13" stroke="#1c9c3c" stroke-width="1.2"/></svg>
        <span>www.kvpartsline.vn</span>
      </li>
      <li class="contact-item">
        <svg class="contact-icon" viewBox="0 0 16 16" aria-hidden="true"><circle cx="8" cy="8" r="6.5" fill="none" stroke="#1c9c3c" stroke-width="1.5"/><ellipse cx="8" cy="8" rx="2.8" ry="6.5" fill="none" stroke="#1c9c3c" stroke-width="1.2"/><path d="M1.5 8h13" stroke="#1c9c3c" stroke-width="1.2"/></svg>
        <span>www.kvpartsline.com</span>
      </li>
    </ul>
  </div>
</section>

</body>
</html>
```